Web Site Design

We need to design the whole web site for our small start up. We sell hospitality and culinary art internships abroad. I did my own design with WIX which is horrible meanwhile I started with my business. You can see it www.brightvoyage-intern.example I will need you to create a new and attractive web site and to leave it working on wix. The internship destinations are United Arab Emirates, Thailand, China, Spain, Brazil and maybe leave a couple of pages for future destinations.You could also get other ideas of other sites that do internships.

Target Market(s)

Students and recent graduates of hospitality and culinary art majors

Industry/Entity Type

Education

Number of Pages Required

5+ page

Requirements
Must have
• Addittional to our program destinations, or to the pages in the current site. The website must contain a page for Universities or Hotels who require our service

```html
<!DOCTYPE html>
<html lang="en">
<head>
<meta charset="utf-8">
<title>BrightVoyage – Hospitality &amp; Culinary Art Internships Abroad</title>
<link rel="stylesheet" href="https://fonts.googleapis.com/css2?family=Montserrat:wght@400;500;600;700&family=Mulish:wght@400;500&display=swap">
<style>
  :root{
    --accent:#f6bc4f;
    --ink:#5b5b5b;
    --ink-soft:#8a8a8a;
    --white:#ffffff;
    --field:#f4f2ee;
  }
  *{box-sizing:border-box;margin:0;padding:0}
  html,body{width:1200px;height:1165px;overflow:hidden;background:var(--white)}
  body{position:relative;font-family:"Montserrat",sans-serif;color:var(--ink)}
  .abs{position:absolute}

  /* Hero */
  .hero{left:0;top:0;width:1200px;height:464px;
    background:radial-gradient(ellipse at 55% 35%,#6b5a4a 0%,#3e342c 45%,#1f1b18 100%)}
  .hero-shade{left:0;top:0;width:1200px;height:464px;background:linear-gradient(rgba(0,0,0,.35),rgba(0,0,0,.05) 30%,rgba(0,0,0,.1))}
  .brand{font-family:"Montserrat",sans-serif;font-weight:600;letter-spacing:-.2px}
  .nav-brand{left:268px;top:14px;font-size:20px;color:var(--accent)}
  .nav{left:578px;top:19px;display:flex;gap:0;font-size:14px;font-weight:500;color:var(--white)}
  .nav a{color:inherit;text-decoration:none;position:absolute;white-space:nowrap}
  .nav a.active{color:var(--accent)}
  .hero-title{left:0;width:1200px;top:131px;text-align:center;color:var(--white);font-size:17.5px;font-weight:600}
  .hero-title span,.accent{color:var(--accent)}
  .hero-rule{left:573px;top:159px;width:73px;height:2px;background:var(--accent)}
  .hero-sub{left:400px;width:400px;top:173px;text-align:center;color:var(--white);font-size:14.5px;font-weight:500;line-height:17px}
  .search{left:360px;top:248px;width:500px;height:33px;background:rgba(255,255,255,.85);border-radius:2px}
  .search-text{left:14px;top:8px;font-size:14px;color:#6f6f6f;font-weight:500}
  .search-btn{left:469px;top:3px;width:27px;height:27px;background:var(--accent);border-radius:2px}

  /* Who we are */
  .section-title{left:0;width:1200px;text-align:center;font-size:18px;font-weight:600}
  .who-title{top:493px;color:var(--ink)}
  .section-sub{left:330px;width:540px;text-align:center;font-family:"Mulish",sans-serif;font-size:12.5px;line-height:16px;color:var(--ink-soft)}
  .who-sub{top:522px}
  .who-photo{left:281px;top:585px;width:230px;height:154px;background:linear-gradient(135deg,#4c4a44 0%,#8a8275 45%,#c9b89a 75%,#9a7a52 100%)}
  .who-heading{left:551px;top:586px;font-size:16px;font-weight:600;color:var(--ink)}
  .who-text{left:551px;top:622px;width:362px;font-family:"Mulish",sans-serif;font-size:11px;line-height:18px;color:var(--ink-soft)}

  /* Apply band */
  .apply{left:0;top:782px;width:1200px;height:246px;
    background:linear-gradient(180deg,#a69a84 0%,#8e8572 45%,#6b6557 80%,#5a5549 100%)}
  .apply-title{top:824px;color:var(--white)}
  .apply-sub{left:445px;width:310px;top:859px;text-align:center;color:var(--white);font-size:14px;line-height:16px;font-weight:500}
  .field{top:932px;width:133px;height:33px;background:var(--field);border-radius:2px;font-family:"Mulish",sans-serif;font-size:13px;color:#9a9a9a;padding:8px 5px}
  .apply-btn{left:782px;top:932px;width:98px;height:33px;background:var(--accent);color:var(--white);font-weight:600;font-size:14.5px;text-align:center;line-height:32px;border-radius:2px}

  /* Footer */
  .foot-brand{left:269px;top:1056px;font-size:19px;color:var(--accent)}
  .copyright{left:269px;top:1088px;font-family:"Mulish",sans-serif;font-size:8.5px;color:var(--ink)}
  .foot-head{top:1061px;font-size:13.5px;font-weight:500;color:var(--accent)}
  .foot-list{list-style:none;font-family:"Mulish",sans-serif;font-size:11px;line-height:18px;color:var(--ink);top:1089px}
  .social{left:812px;top:1088px;display:flex;gap:12px}
  .social i{display:block;width:14px;height:14px;border-radius:50%;background:#8a8a8a}
</style>
</head>
<body>

<!-- Hero -->
<div class="abs hero" role="img" aria-label="Photo of a barista pouring coffee behind a busy café counter"></div>
<div class="abs hero-shade"></div>
<div class="abs brand nav-brand">BrightVoyage</div>
<nav class="abs nav">
  <a class="active" href="#" style="left:0">Home</a>
  <a href="#" style="left:70px">Destinations</a>
  <a href="#" style="left:184px">About Us</a>
  <a href="#" style="left:276px">Contact Us</a>
</nav>
<h1 class="abs hero-title">Hospitality &amp; Culinary Art Internships <span>Abroad</span>.</h1>
<div class="abs hero-rule"></div>
<p class="abs hero-sub">Lorem ipsum dolor sit amet, consectetur adipiscing elit. Mauris lobortis tincidunt justo ac dapibus.</p>
<div class="abs search">
  <span class="abs search-text">Search for internship...</span>
  <div class="abs search-btn">
    <svg width="27" height="27" viewBox="0 0 27 27" aria-hidden="true">
      <circle cx="12.5" cy="12.5" r="4.5" fill="none" stroke="#6b5a3a" stroke-width="1.3"/>
      <line x1="15.8" y1="15.8" x2="19" y2="19" stroke="#6b5a3a" stroke-width="1.3" stroke-linecap="round"/>
    </svg>
  </div>
</div>

<!-- Who we are -->
<h2 class="abs section-title who-title">Who we <span class="accent">Are</span></h2>
<p class="abs section-sub who-sub">Lorem ipsum dolor sit amet, consectetur adipiscing elit. Mauris lobortis tincidunt justo ac dapibus</p>
<div class="abs who-photo" role="img" aria-label="Photo of a smiling intern at a laptop in a bright office"></div>
<h3 class="abs who-heading"><span class="accent">We</span> provide excelent expirience for <span class="accent">All</span> Interns</h3>
<p class="abs who-text">Lorem ipsum dolor sit amet, consectetur adipiscing elit. Mauris lobortis tincidunt justo ac dapibus. Vestibulum ante ipsum primis in faucibus orci luctus et ultrices posuere cubilia Curae; Suspendisse sed accumsan mi. Duis volutpat condimentum fermentum. Duis consequat sapien id eleifend faucibus. Pellentesque habitant morbi tristique senectus et netus et malesuada fames ac turpis egestas.</p>

<!-- Apply -->
<div class="abs apply" role="img" aria-label="Photo of hot-air balloons over misty temple plains at sunrise"></div>
<h2 class="abs section-title apply-title">Apply for Internship <span class="accent">Now.</span></h2>
<p class="abs apply-sub">Lorem ipsum dolor sit amet, consectetur adipiscing elit. Mauris lobortis tincidunt justo ac dapibus.</p>
<div class="abs field" style="left:331px">Name</div>
<div class="abs field" style="left:482px">Email</div>
<div class="abs field" style="left:633px">Phone Number</div>
<div class="abs apply-btn">Apply</div>

<!-- Footer -->
<div class="abs brand foot-brand">BrightVoyage</div>
<div class="abs copyright">© 2016 BrightVoyage.</div>
<h4 class="abs foot-head" style="left:530px">Links</h4>
<ul class="abs foot-list" style="left:531px"><li>Home</li><li>Destinations</li><li>About Us</li><li>Contact Us</li></ul>
<h4 class="abs foot-head" style="left:667px">Info</h4>
<ul class="abs foot-list" style="left:665px"><li>Privacy Policy</li><li>Disclaimer</li><li>Terms &amp; Conditions</li><li>Help</li></ul>
<h4 class="abs foot-head" style="left:816px">Social</h4>
<div class="abs social" aria-label="Social links"><i></i><i></i><i></i></div>

</body>
</html>
```